Used Car Dealer seeks an Amazing Business Card Design

We are looking for a business card design that incorporates our logo and grabs the attention of anyone we give the business card to.

Looking to use the same colors as the logo. Our Logo choice is the black background with Red and Silver/Grey Lettering.

We also would like to see some embossed designs.

Target Market(s)

Used Car Buyers, Automotive, Auto

Industry/Entity Type

Automotive

Contact Information for Business Card

BVEL7K
Gordon Whitlock
482 Tarrow Lane
Suite 207
Halvern, GA 30419
Office (628) 555-0142
Cell (628) 555-0187
bvel7kga@quellmail.com
www.bvel7kga.com

Colors
ffffff
ee3036

Requirements
Must have
• Must include our logo (Black Background with Red and Silver/Grey Lettering)
Nice to have
• Embossed Design. Can be Single or Double Sided.

```html
<!DOCTYPE html>
<html lang="en">
<head>
<meta charset="utf-8">
<title>BVEL7K Business Card</title>
<link href="https://fonts.googleapis.com/css2?family=Open+Sans:wght@600;700&display=swap" rel="stylesheet">
<style>
  :root {
    --stage: #bdbdbd;
    --card-black: #161616;
    --brand-red: #ee3036;
    --panel-red: #d4202c;
    --deep-red: #6e0c10;
    --strip-grey: #a3a3a3;
    --strip-shade: #8c8c8c;
    --white: #ffffff;
    --icon-dark: #2a1012;
  }
  * { margin: 0; padding: 0; box-sizing: border-box; }
  html, body { width: 1000px; height: 1200px; overflow: hidden; }
  body {
    background: var(--stage);
    font-family: "Open Sans", Arial, sans-serif;
    position: relative;
  }
  .card {
    position: absolute;
    left: 107px;
    width: 748px;
    height: 394px;
    background: var(--card-black);
    overflow: hidden;
    box-shadow: 0 28px 40px rgba(0,0,0,0.28);
  }
  .card-front { top: 104px; }
  .card-back { top: 707px; }

  .front-wave { position: absolute; left: 0; top: 0; width: 748px; height: 394px; }

  .wordmark {
    position: absolute;
    color: var(--white);
    font-weight: 700;
    letter-spacing: 1px;
    line-height: 1;
  }
  .card-front .wordmark { left: 0; width: 748px; top: 162px; text-align: center; font-size: 72px; }
  .card-back .wordmark { left: 30px; width: 300px; top: 188px; text-align: center; font-size: 54px; }

  .back-panels { position: absolute; left: 0; top: 0; width: 748px; height: 394px; }

  .contact {
    position: absolute;
    left: 391px;
    top: 58px;
    color: var(--white);
  }
  .contact-name { font-size: 24px; font-weight: 700; margin-bottom: 21px; }
  .contact-group {
    display: flex;
    align-items: center;
    margin-bottom: 14px;
  }
  .contact-icon { width: 28px; height: 28px; margin-right: 19px; flex: none; }
  .contact-lines { font-size: 16px; font-weight: 600; line-height: 32px; }
</style>
</head>
<body>

<section class="card card-front">
  <svg class="front-wave" viewBox="0 0 748 394" aria-hidden="true">
    <defs>
      <linearGradient id="waveRed" x1="0" y1="0" x2="1" y2="0">
        <stop offset="0" stop-color="var(--deep-red)"/>
        <stop offset="0.45" stop-color="var(--brand-red)"/>
        <stop offset="1" stop-color="var(--brand-red)"/>
      </linearGradient>
    </defs>
    <path d="M0 268 Q374 450 748 262 L748 394 L0 394 Z" fill="url(#waveRed)"/>
  </svg>
  <div class="wordmark">BVEL7K</div>
</section>

<section class="card card-back">
  <svg class="back-panels" viewBox="0 0 748 394" aria-hidden="true">
    <rect x="333" y="0" width="36" height="394" fill="var(--strip-grey)"/>
    <path d="M367 0 H748 V394 H367 V322 H351 V128 H367 Z" fill="var(--panel-red)"/>
    <path d="M333 118 L351 128 L351 322 L333 332 Z" fill="var(--strip-shade)"/>
  </svg>

  <div class="wordmark">BVEL7K</div>

  <div class="contact">
    <div class="contact-name">Gordon Whitlock</div>

    <div class="contact-group">
      <svg class="contact-icon" viewBox="0 0 28 28" aria-hidden="true">
        <path d="M14 2 C8.5 2 5 6 5 10.5 C5 16 14 27 14 27 C14 27 23 16 23 10.5 C23 6 19.5 2 14 2 Z" fill="var(--icon-dark)"/>
        <circle cx="14" cy="10.5" r="3.6" fill="var(--panel-red)"/>
      </svg>
      <div class="contact-lines">482 Tarrow Lane Suite 207<br>Halvern, GA 30419</div>
    </div>

    <div class="contact-group">
      <svg class="contact-icon" viewBox="0 0 28 28" aria-hidden="true">
        <path d="M7 3 L11 3 L13 9 L10 11 C11.5 15 13.5 17 17 18.5 L19 15.5 L25 17.5 L25 21.5 C25 23.5 23 25 21 25 C12 24 4 16 3 7 C3 5 5 3 7 3 Z" fill="var(--icon-dark)"/>
      </svg>
      <div class="contact-lines">Office (628) 555-0142<br>Cell (628) 555-0187</div>
    </div>

    <div class="contact-group">
      <svg class="contact-icon" viewBox="0 0 28 28" aria-hidden="true">
        <rect x="3" y="7" width="22" height="15" fill="none" stroke="var(--icon-dark)" stroke-width="2"/>
        <path d="M3 7 L14 16 L25 7" fill="none" stroke="var(--icon-dark)" stroke-width="2"/>
      </svg>
      <div class="contact-lines">bvel7kga@quellmail.com<br>www.bvel7kga.com</div>
    </div>
  </div>
</section>

</body>
</html>
```